TDM accounting firm Canada - Modern and professional business cards

To use our existing logo and create a modern looking business card.
We are looking for double sided style.
Silver-metallic background - our logo in front (reverse side)
The reverse side from the attachment- big logo over silver-metallic background is preferred.
we would like to have a business card template that can be modified to change names, addresses, and other

Industry/Entity Type

Accounting

Contact Information for Business Card

Reverse side silver-metallic finish

Font styles to use
Sans Serif

Requirements
Must have
• Reverse side silver-metallic finish
• Modern look

```html
<!DOCTYPE html>
<html lang="en">
<head>
<meta charset="utf-8">
<title>TDM Business Cards</title>
<link href="https://fonts.googleapis.com/css2?family=Arimo:wght@400;700&display=swap" rel="stylesheet">
<style>
  :root {
    --page: #ecebe8;
    --blue: #1a5cb8;
    --green: #2d8a3a;
    --silver-light: #f4f4f4;
    --silver-mid: #d9dadb;
    --silver-dark: #bfc1c3;
    --shadow: rgba(0, 0, 0, 0.22);
  }
  * { margin: 0; padding: 0; box-sizing: border-box; }
  html, body {
    width: 1200px; height: 800px; overflow: hidden;
    background: var(--page);
    font-family: "Arimo", Arial, sans-serif;
  }
  .canvas {
    position: relative; width: 1200px; height: 800px;
    display: flex; align-items: center; justify-content: center; gap: 60px;
  }
  .card {
    position: relative; width: 500px; height: 286px;
    border-radius: 3px;
    background:
      repeating-linear-gradient(0deg, rgba(255,255,255,0.18) 0 1px, rgba(0,0,0,0.03) 1px 3px),
      linear-gradient(120deg, var(--silver-dark) 0%, var(--silver-light) 35%, var(--silver-mid) 60%, var(--silver-light) 80%, var(--silver-dark) 100%);
    box-shadow: 0 10px 24px var(--shadow);
    color: var(--blue);
  }
  .wordmark { display: flex; align-items: center; gap: 10px; }
  .wordmark-symbol {
    font-weight: 700; color: var(--blue); letter-spacing: 1px; line-height: 1;
  }
  .wordmark-divider { width: 2px; align-self: stretch; background: var(--green); }
  .wordmark-name {
    font-weight: 700; text-transform: uppercase; line-height: 1.02; color: var(--blue);
  }

  /* Reverse side */
  .card-back .wordmark {
    position: absolute; left: 70px; top: 82px;
  }
  .card-back .wordmark-symbol { font-size: 66px; }
  .card-back .wordmark-name { font-size: 22px; }
  .card-back .website {
    position: absolute; left: 290px; top: 196px;
    font-size: 15px; font-weight: 700; color: var(--blue);
  }

  /* Front side */
  .card-front .wordmark { position: absolute; left: 30px; top: 26px; gap: 8px; }
  .card-front .wordmark-symbol { font-size: 38px; }
  .card-front .wordmark-name { font-size: 13.5px; }
  .person { position: absolute; left: 30px; top: 132px; }
  .person-name {
    font-size: 17px; font-weight: 700; color: var(--blue);
    padding-bottom: 3px; border-bottom: 1.5px solid var(--green);
    width: 290px;
  }
  .person-title {
    margin-top: 3px; font-size: 12.5px; font-weight: 700;
    text-transform: uppercase; color: var(--green); letter-spacing: 0.3px;
  }
  .contacts { position: absolute; left: 30px; top: 206px; list-style: none; }
  .contacts li {
    display: flex; align-items: center; gap: 12px;
    font-size: 13px; font-weight: 700; color: var(--blue);
    height: 22px;
  }
  .contacts svg { width: 15px; height: 15px; fill: var(--green); }
  .card-front .website {
    position: absolute; right: 32px; bottom: 26px;
    font-size: 14px; font-weight: 700; color: var(--blue);
  }
</style>
</head>
<body>
<main class="canvas">
  <section class="card card-back" aria-label="Business card reverse side">
    <div class="wordmark">
      <span class="wordmark-symbol">TDM</span>
      <span class="wordmark-divider"></span>
      <span class="wordmark-name">Eastvale<br>Professional<br>Corporation</span>
    </div>
    <p class="website">www.tdm-cpa.com</p>
  </section>

  <section class="card card-front" aria-label="Business card front side">
    <div class="wordmark">
      <span class="wordmark-symbol">TDM</span>
      <span class="wordmark-divider"></span>
      <span class="wordmark-name">Eastvale<br>Professional<br>Corporation</span>
    </div>
    <div class="person">
      <p class="person-name">Marco Delgado CPA, CGA.</p>
      <p class="person-title">Principal and Senior Consultant</p>
    </div>
    <ul class="contacts">
      <li>
        <svg viewBox="0 0 16 16" aria-hidden="true"><path d="M4.5 0h7A1.5 1.5 0 0 1 13 1.5v13a1.5 1.5 0 0 1-1.5 1.5h-7A1.5 1.5 0 0 1 3 14.5v-13A1.5 1.5 0 0 1 4.5 0zM5 2v10h6V2zm3 11a1 1 0 1 0 0 2 1 1 0 0 0 0-2z"/></svg>
        (780) 555-0142
      </li>
      <li>
        <svg viewBox="0 0 16 16" aria-hidden="true"><path d="M1 5c0-2 3-3 7-3s7 1 7 3v1.5h-4V5H5v1.5H1zM4 8h8l2 6H2zm4 1.5a2 2 0 1 0 0 4 2 2 0 0 0 0-4z"/></svg>
        (780) 555-0187
      </li>
      <li>
        <svg viewBox="0 0 16 16" aria-hidden="true"><path d="M1 3h14v1.2L8 9 1 4.2zm0 2.6 7 4.8 7-4.8V13H1z"/></svg>
        marco@tdm-cpa.com
      </li>
    </ul>
    <p class="website">www.tdm-cpa.com</p>
  </section>
</main>
</body>
</html>
```